Dr Selwyn aesthetics - Radiance Refined

I need a logo design for a new aesthetics business in London. I am specialised in Botox, Dermal Fillers & Skin Pigmentation treatment. The slogan is Radiance Refined. I would like some of the writing on the card to be embossed. I would like a very elegant design with the following detail:

1. White and gray scale background. For the font colour try gold OR silver shades.
2. The business involves working on the face mostly. Anything that can be done with letter 'M'? Or any other logo?
3. The front of the card should have Dr Selwyn Aesthetics and the slogan 'Radiance Refined'. The back should have my full name (Dr Selwyn Tarkett), qualifications (MBBS MSC BSC), my website (www.thebrindlecliniccollective.example), telephone number & email.
4. The back should also say treatments offered: ANTI-WRINKLE INJECTIONS. DERMAL FILLERS, LIP ENHANCEMENT, HYPERHYDROSIS. SKIN PIGMENTATION

Thank you very much
Updates

Project Deadline Extended
Reason: Delays in market research response. I would be grateful for an extension please. Many thanks

Target Market(s)

Female and male aged 18 and above

Industry/Entity Type

Business

Contact Information for Business Card

Elegant design. Square corners. British standard size. Horizontal design. Should contain the slogan, contact details.

Font styles to use
Script

Colors
c9c9c9
fbed22
ffffff
f5f5f5
000000

Requirements
Must have
• All that's mentioned above
Nice to have
• A logo with the outline of a female face. Or anything that can be done with the letter M of Selwyn.
Should not have
• No colours like green / purple / orange

```html
<!DOCTYPE html>
<html lang="en">
<head>
<meta charset="utf-8">
<title>Dr Selwyn Aesthetics – Business Card</title>
<link rel="stylesheet" href="https://fonts.googleapis.com/css2?family=Oswald:wght@500&family=Open+Sans:wght@400;600&display=swap">
<style>
  :root {
    --stage: #e9e9e9;
    --card-white: #ffffff;
    --card-grey: #f5f5f5;
    --card-shade: #c9c9c9;
    --accent-gold: #b8962e;
    --accent-silver: #a8a8a8;
    --text-dark: #1a1a1a;
    --text-mid: #555555;
    --mark-faint: #ececec;
  }
  * { margin: 0; padding: 0; box-sizing: border-box; }
  html, body { width: 1200px; height: 844px; overflow: hidden; }
  body {
    background: var(--stage);
    position: relative;
    font-family: "Open Sans", Arial, sans-serif;
  }
  .card {
    position: absolute;
    top: 254px;
    width: 520px;
    height: 336px;
    overflow: hidden;
    box-shadow: 0 8px 24px rgba(0,0,0,0.18);
  }
  /* ---------- Contact side ---------- */
  .card--contact {
    left: 50px;
    background: linear-gradient(160deg, var(--card-white) 0%, var(--card-grey) 55%, #e4e4e4 100%);
  }
  .band {
    position: absolute;
    left: 0;
    right: 0;
    height: 13px;
    background: var(--accent-gold);
  }
  .band--top { top: 10px; }
  .band--bottom { bottom: 10px; }
  .faint-mark {
    position: absolute;
    left: -70px;
    top: 150px;
    width: 230px;
    height: 230px;
    border-radius: 50%;
    background: var(--mark-faint);
  }
  .treatments {
    position: absolute;
    left: 22px;
    top: 42px;
    width: 190px;
  }
  .treatments__title {
    font-size: 10px;
    font-weight: 600;
    letter-spacing: 1.4px;
    color: var(--accent-gold);
    text-transform: uppercase;
    margin-bottom: 4px;
  }
  .treatments__list {
    list-style: none;
    font-size: 9.5px;
    line-height: 14px;
    letter-spacing: 0.6px;
    color: var(--text-mid);
    text-transform: uppercase;
  }
  .holder {
    position: absolute;
    left: 250px;
    top: 96px;
  }
  .holder__name {
    font-weight: 600;
    font-size: 17px;
    color: var(--accent-gold);
    text-transform: uppercase;
    letter-spacing: 0.3px;
    padding-bottom: 2px;
    border-bottom: 1px solid var(--accent-silver);
  }
  .holder__quals {
    font-size: 12.5px;
    color: var(--text-dark);
    margin-top: 3px;
    padding-left: 22px;
    letter-spacing: 1px;
  }
  .contact-list {
    position: absolute;
    left: 110px;
    width: 400px;
    top: 206px;
    list-style: none;
    text-align: center;
    color: var(--text-dark);
    font-size: 13px;
    line-height: 17px;
  }
  .contact-list__address { margin-top: 10px; font-size: 13.5px; }
  /* ---------- Brand side ---------- */
  .card--brand {
    left: 630px;
    background: radial-gradient(ellipse at 45% 50%, var(--card-white) 0%, var(--card-grey) 55%, var(--card-shade) 130%);
  }
  .tab {
    position: absolute;
    width: 22px;
    height: 30px;
    background: var(--accent-gold);
  }
  .tab--left { left: 0; top: 180px; border-right: 4px solid var(--accent-silver); }
  .tab--right { right: 0; top: 66px; border-left: 4px solid var(--accent-silver); }
  .brand {
    position: absolute;
    left: 100px;
    top: 138px;
    display: flex;
    align-items: center;
    gap: 14px;
  }
  .brand__dot {
    width: 52px;
    height: 52px;
    border-radius: 50%;
    background: var(--accent-gold);
  }
  .brand__name {
    font-family: "Oswald", "Arial Narrow", sans-serif;
    font-weight: 500;
    font-size: 23px;
    line-height: 26px;
    color: var(--accent-gold);
    text-transform: uppercase;
  }
  .brand__slogan {
    font-size: 13px;
    color: var(--text-mid);
    letter-spacing: 3.2px;
    text-transform: uppercase;
    margin-top: 2px;
  }
</style>
</head>
<body>
  <section class="card card--contact" aria-label="Contact side">
    <div class="band band--top"></div>
    <div class="faint-mark" aria-hidden="true"></div>
    <div class="treatments">
      <p class="treatments__title">Treatments</p>
      <ul class="treatments__list">
        <li>Anti-wrinkle injections</li>
        <li>Dermal fillers</li>
        <li>Lip enhancement</li>
        <li>Hyperhydrosis</li>
        <li>Skin pigmentation</li>
      </ul>
    </div>
    <div class="holder">
      <p class="holder__name">Dr Selwyn Tarkett</p>
      <p class="holder__quals">MBBS MSC BSC</p>
    </div>
    <ul class="contact-list">
      <li>020-7946-0812</li>
      <li>020-7946-0377</li>
      <li>hello@brindleclinic.example</li>
      <li>www.thebrindlecliniccollective.example</li>
      <li class="contact-list__address">18 Harrow Lane | London, UK | W1 4QX</li>
    </ul>
    <div class="band band--bottom"></div>
  </section>

  <section class="card card--brand" aria-label="Brand side">
    <div class="tab tab--left"></div>
    <div class="tab tab--right"></div>
    <div class="brand">
      <span class="brand__dot" aria-hidden="true"></span>
      <div>
        <p class="brand__name">Dr Selwyn Aesthetics</p>
        <p class="brand__slogan">Radiance Refined</p>
      </div>
    </div>
  </section>
</body>
</html>
```